A corporate Christmas card for Ferncrest University

We need a Christmas card design for a University. We are a private university with a reputation for academic excellence. We also have a strong christian identity. The final design must communicate elegance, grace and our Christian background.

Target Market(s)

managers and company executives; people with at least a college degree; thirty to 50 years old

Industry/Entity Type

University

Colors

Designer to choose colors to be used in the design.

Requirements
Must have
• The card must have 4 pages and use only the photos attached.
Size of card when folded: 5" x 7"
An image of the nativity
The University's name and logo
The University's URL (www.fcu.edu.zq)
The expression 'Merry Christmas'
One of the inner pages must have the following discreetly placed:
"‘Look, the virgin shall conceive and bear a son, and they shall name him Emmanuel’, which means, ‘God is with us.’

Matthew chapter 1, vs 23"
Nice to have
• The University's name and logo and the University's URL (www.fcu.edu.zq) should be on the back page.
Should not have
• The expression 'seasons greetings' or 'happy holidays'

```html
<!DOCTYPE html>
<html lang="en">
<head>
<meta charset="utf-8">
<title>Ferncrest University – Christmas Card Inner Page</title>
<link href="https://fonts.googleapis.com/css2?family=Sorts+Mill+Goudy:ital@0;1&display=swap" rel="stylesheet">
<style>
  :root {
    --ink-black: #0b0b0b;
    --stroke-grey: #1c1c1c;
    --stroke-dark: #050505;
    --scripture-orange: #ff8a0a;
  }
  * { margin: 0; padding: 0; box-sizing: border-box; }
  html, body {
    width: 858px;
    height: 1200px;
    overflow: hidden;
    background: var(--ink-black);
  }
  .card-page {
    position: relative;
    width: 858px;
    height: 1200px;
    overflow: hidden;
    background: var(--ink-black);
    font-family: "Sorts Mill Goudy", "Goudy Old Style", Georgia, serif;
    color: var(--scripture-orange);
  }
  .brush-texture {
    position: absolute;
    inset: 0;
    background:
      linear-gradient(176deg,
        var(--stroke-grey) 0%, var(--stroke-dark) 6%, var(--stroke-grey) 11%,
        var(--stroke-dark) 17%, var(--stroke-grey) 24%, var(--stroke-dark) 31%,
        var(--stroke-grey) 39%, var(--stroke-dark) 47%, var(--stroke-grey) 55%,
        var(--stroke-dark) 63%, var(--stroke-grey) 71%, var(--stroke-dark) 79%,
        var(--stroke-grey) 87%, var(--stroke-dark) 94%, var(--stroke-grey) 100%);
  }
  .scripture-quote {
    position: absolute;
    left: 63px;
    top: 270px;
    font-style: italic;
    font-size: 46px;
    line-height: 69px;
    white-space: nowrap;
  }
  .scripture-reference {
    position: absolute;
    left: 60px;
    top: 689px;
    font-style: italic;
    font-size: 74px;
    line-height: 1;
    white-space: nowrap;
  }
</style>
</head>
<body>
  <main class="card-page">
    <div class="brush-texture" role="img" aria-label="Dark black brush-stroke painted texture background"></div>
    <p class="scripture-quote">‘Look, the virgin shall conceive and<br>bear a son, and they shall name him<br>Emmanuel’, which means, ‘God is<br>with us.’</p>
    <p class="scripture-reference">Matthew chapter 1, vs 23</p>
  </main>
</body>
</html>
```